Flyer-Design für Hausarztpraxis
Zielgruppe
Hausarztpraxis, Zielgruppe junge Patienten ...
Aufgabenstellung
Mein aktueller Flyer sollte modernisiert werden ... Texte können gern überarbeitet werden... Neue Fotos der Praxis werden noch gemacht. DH die Datei sollte so sein, dass ich die Fotos anpassen kann hinterher
Farbe gern in dem schönen Magenta wie das Logo
Aufbau des Flysers sollte ebenfalls optimiert werden.

```html
<!DOCTYPE html>
<html lang="de">
<head>
<meta charset="utf-8">
<title>Flyer Hausarztpraxis Dr. med. Marlene Hofstetter</title>
<link href="https://fonts.googleapis.com/css2?family=Poppins:wght@300;400;600;700;800&display=swap" rel="stylesheet">
<style>
:root{
  --magenta:#dc2a55;
  --magenta-dark:#c41f49;
  --ink:#1e1e1e;
  --band:rgba(40,40,40,.88);
  --paper:#ffffff;
  --stage:#ececec;
  --photo-grey:linear-gradient(160deg,#d8d8d8,#8d8d8d 55%,#5a5a5a);
}
*{margin:0;padding:0;box-sizing:border-box}
html,body{width:1200px;height:2578px;overflow:hidden;background:var(--paper)}
body{position:relative;font-family:'Poppins',sans-serif;color:var(--ink)}
.stage{position:absolute;left:67px;top:67px;width:1066px;height:800px;background:var(--stage)}
.spread{position:absolute;left:129px;width:941px;height:667px;background:var(--paper);box-shadow:0 6px 14px rgba(0,0,0,.35);overflow:hidden}
.spread--inside{top:994px}
.spread--outside{top:1783px}
.panel{position:absolute;top:0;height:100%}
.photo{position:absolute;background:var(--photo-grey)}
.photo--colour{background:linear-gradient(160deg,#f2f2f2,#c9c6c0 60%,#8f8c88)}
.photo--portrait{background:linear-gradient(180deg,#f1eef0,#e4c9cf 60%,#c98a9a)}
.welcome{left:0;width:313px;background:var(--magenta);color:#fff}
.welcome .greet{position:absolute;left:44px;top:330px;width:240px;font-size:11.5px;line-height:14.5px;font-weight:300}
.welcome .greet strong{font-weight:600}
.welcome .greet p{margin-bottom:13px}
.mark{position:absolute;width:24px;height:24px;border:2px solid #fff;border-radius:50%}
.headline-band{position:absolute;left:0;background:var(--band);color:#fff;font-weight:700;text-transform:uppercase}
.news .headline-band{top:173px;width:628px;height:77px;padding:22px 0 0 92px;font-size:25px;letter-spacing:.3px}
.col{position:absolute;font-size:11.5px;line-height:13.4px;font-weight:400;width:260px}
.col p{margin-bottom:13px}
.hl{color:var(--magenta)}
.indent{padding-left:12px}
.service h3,.service h4{color:var(--magenta);font-weight:700;text-align:center;font-size:13.5px;line-height:20px}
.list{list-style:none;font-size:11.5px;line-height:15.6px}
.list li::before{content:"• "}
.phone .headline-band{top:130px;width:313px;height:70px;text-align:center;padding-top:8px}
.phone .headline-band .big{display:block;font-size:22px;line-height:26px}
.phone .headline-band .small{display:block;font-size:14.5px;line-height:18px}
.numbers{position:absolute;left:20px;top:242px;width:270px;list-style:none;font-size:12px;line-height:20px}
.numbers li{display:flex;justify-content:space-between}
.numbers li span:first-child::before{content:"• "}
.footer-band{position:absolute;left:0;bottom:0;width:941px;height:36px;background:var(--magenta);border-top:3px solid #fff;box-shadow:0 -2px 0 var(--magenta)}
.footer-band .mark{left:458px;top:5px}
.brand{position:absolute;left:0;top:0;width:313px;height:130px;text-align:center}
.brand .dot{width:36px;height:36px;border:3px solid var(--magenta);border-radius:50%;margin:18px auto 10px}
.brand .line{font-size:9px;letter-spacing:3px;color:#555;text-transform:uppercase}
.brand .name{font-size:14px;font-weight:400;color:var(--magenta);text-transform:uppercase;letter-spacing:.5px;margin-top:3px}
.contact{position:absolute;left:0;top:448px;width:313px;text-align:center;font-size:12px;line-height:14.5px}
.contact strong{color:var(--magenta);font-weight:600;display:block}
.contact .gap{height:14px}
</style>
</head>
<body>
<div class="stage"></div>

<section class="spread spread--inside">
  <div class="panel welcome">
    <div class="photo photo--portrait" style="left:40px;top:36px;width:233px;height:240px" role="img" aria-label="Porträtfoto der Ärztin vor hellem Hintergrund"></div>
    <div class="greet">
      <p><strong>Liebe Patientinnen und Patienten,</strong></p>
      <p>Zum 1. Oktober habe ich nach fast zwei Jahren intensiver Einarbeitung die Praxis von Herrn <strong>Dr.</strong> Weidner übernommen.</p>
      <p>In diesem Flyer sehen sie all unsere Neuerungen rund um die Praxis.</p>
      <p>Ich werde Sie mit Leidenschaft medizinisch betreuen und auch mit Herz für Ihre Probleme da sein!</p>
      <p><strong>Dr. Marlene Hofstetter</strong></p>
    </div>
    <div class="mark" style="left:144px;top:580px"></div>
  </div>
  <div class="panel news" style="left:313px;width:628px">
    <div class="photo" style="left:0;top:0;width:628px;height:250px" role="img" aria-label="Schwarzweißfoto der Fachwerkhäuser mit Apotheke"></div>
    <div class="headline-band">Alle Neuerungen auf einen Blick</div>
    <div class="col" style="left:38px;top:292px">
      <p>Eine unserer sicher für Sie entscheidensten Veränderung sind unsere neuen <span class="hl">Praxisöffnungszeiten.</span></p>
      <p class="indent">Mo 8-11:30 sowie 14-17 Uhr<br>Die 8-13 Uhr<br>Mi 8-13 Uhr<br>Do 8-11:30 sowie 14-18 Uhr<br>Fr 8-11:30</p>
      <p><span class="hl">Telefonisch</span> erreichen Sie uns täglich von 8:00 - 11:00 Uhr sowie Montags und Donnertags von 14:00 - 16:00 Uhr</p>
      <p>Unsere <span class="hl">Laborzeiten</span> sind nun vor der eigentlichen Sprechstunde von 7:15 - 8:00 Uhr. Dazu kommt, das Sie inzwichen die Möglichkeit haben, auch über unsere Website www.hausarzt-talheim.de, <span class="hl">online Termine</span> vereinbaren können.</p>
      <p><span class="hl">Rezepte</span> sollten ein Tag vor Abholung auf unsere Rezepthotline gesprochen werden, oder in den neuen <span class="hl">Briefkasten im Hausflur</span> eingeworfen werden. Diese werden dann</p>
    </div>
    <div class="col" style="left:332px;top:292px;width:250px">
      <p>nach der Sprechzeit für sie fertiggestellt. Wie Sie vielleicht feststellen konnten haben wir eine neue <span class="hl">Praxissoftware un Hardware</span> um die Praxisabläufe zu optimieren und Ihnen kürzere Wartezen anbieten zu können. Über unseren TV im Wartezimmer sehen sie immer alle Neuigkeiten, wie Urlaube oder Kurse.</p>
      <p>Inzwischen können wir auch <span class="hl">Ultraschallunterschungen</span> der Schilddrüse, des Bauches sowie der Gefäße nach DEGUM 2 Leitlinie anbieten.<br>Es besteht auch die Möglichkeit außerhalb der kassenärztlichen Leitungen <span class="hl">Check- UPs</span> wahrzunehmen, wenn Sie es wünschen! Zum Beispiel ein erweiterter Frauem oder Männer Check.</p>
      <p>Im Bereich der Ästhetik bieten wir Ihnen <span class="hl">Hyaloronsäure- Filler</span> im Gesicht zur Faltenenminimierung an.<br>Ebenfalls neu führen wir Einzel und Gruppenschulungen mit autogenem <span class="hl">Training</span> durch.</p>
    </div>
  </div>
</section>

<section class="spread spread--outside">
  <div class="panel service" style="left:0;width:313px">
    <div class="photo photo--colour" style="left:0;top:0;width:313px;height:169px" role="img" aria-label="Farbfoto des Wartezimmers mit Stühlen und Bildern"></div>
    <h3 style="position:absolute;left:0;top:192px;width:313px">Unser Leistungsspektrum</h3>
    <ul class="list" style="position:absolute;left:26px;top:232px">
      <li>Vollständige hausärztliche Versorgung</li>
      <li>Gesundheitsvorsorge</li>
      <li>Krebsvorsorge</li>
      <li>EKG und Ergometrie</li>
      <li>Sonographie Bauch, Schilddrüse, Gefäße</li>
      <li>Langzeitblutdruckmessung</li>
      <li>Lungenfunktionsprüfung</li>
      <li>Laboruntersuchungen</li>
      <li>Sämtliche Impfungen</li>
      <li>Kleine operative Eingriffe</li>
      <li>Wundversorgung</li>
      <li>Autogenes Training</li>
      <li>Neuraltherapie</li>
    </ul>
    <h4 style="position:absolute;left:0;top:458px;width:313px">Zusätzliche individuelle<br>Gesundheitsleistungen</h4>
    <ul class="list" style="position:absolute;left:26px;top:517px">
      <li>Ästhetiche Anwendungen mittels<br>&nbsp;&nbsp;Hyaloronsäurefillern im Gesicht</li>
      <li>Infusionsbehandlungen</li>
      <li>Depressionstherapie</li>
      <li>Sportuntersuchungen</li>
      <li>Patientenverfügungen</li>
    </ul>
  </div>
  <div class="panel phone" style="left:313px;width:314px">
    <div class="photo" style="left:0;top:0;width:314px;height:200px" role="img" aria-label="Schwarzweißfoto von Fachwerkgiebeln"></div>
    <div class="headline-band"><span class="big">Nützlizhe</span><span class="small">Telefonnummern</span></div>
    <ul class="numbers">
      <li><span>Praxis Dr. Hofstetter</span><span>4100</span></li>
      <li><span>Rettungsdienst</span><span>112</span></li>
      <li><span>Linden-Apotheke Talheim</span><span>27455</span></li>
      <li><span>Polizei/ Notruf</span><span>110</span></li>
      <li><span>Giftnotruf</span><span>0761/55501234</span></li>
      <li><span>Krankenhaus Talheim</span><span>170</span></li>
      <li><span>Ärztlicher Bereitschaftsdienst</span><span>116117</span></li>
    </ul>
    <div class="photo photo--colour" style="left:0;top:428px;width:314px;height:206px" role="img" aria-label="Farbfoto des Empfangstresens der Praxis"></div>
  </div>
  <div class="panel" style="left:627px;width:314px">
    <div class="brand">
      <div class="dot"></div>
      <div class="line">Hausarztpraxis</div>
      <div class="name">Dr. med. Marlene Hofstetter</div>
    </div>
    <div class="photo" style="left:0;top:130px;width:314px;height:298px" role="img" aria-label="Schwarzweißfoto der Altstadt mit Fachwerkhaus und Turm"></div>
    <div class="contact">
      <strong>Dr. med. Marlene Hofstetter</strong>
      Fachärztin f. Allgemeinmedizen<br>Lindenweg 14 - 72100 Talheim
      <div class="gap"></div>
      <strong>Sprechzeiten</strong>
      Mo 8-11:30 sowie 14-17 Uhr<br>Die 8-13 Uhr<br>Mi 8-13 Uhr<br>Do 8-11:30 sowie 14-18 Uhr<br>Fr 8-11:30
    </div>
  </div>
  <div class="footer-band"><div class="mark"></div></div>
</section>
</body>
</html>
```